The Plaster & Resonance Craftworks Inc (PRCI)

Create a LOGO and Business Card design.

Colors: Black, Bright Yellow & Red

Description of company: commercial carpentry, metal framing, drywall, taping/spackling, demolition, rough/finish carpentry.

Target Market(s)

developers, architects, general contractors, construction managers

Industry/Entity Type

Business

```html
<!DOCTYPE html>
<html lang="en">
<head>
<meta charset="utf-8">
<title>PRCI Business Card</title>
<link rel="stylesheet" href="https://fonts.googleapis.com/css2?family=Questrial&family=Libre+Baskerville&family=Arimo&display=swap">
<style>
  :root {
    --bg: #e6e6e6;
    --card-black: #000000;
    --card-white: #ffffff;
    --accent-red: #e0201f;
    --text-white: #ffffff;
  }
  * { margin: 0; padding: 0; box-sizing: border-box; }
  html, body { width: 1200px; height: 900px; overflow: hidden; background: var(--bg); }
  .canvas { position: relative; width: 1200px; height: 900px; }

  .card { position: absolute; width: 650px; height: 395px; border-radius: 16px; overflow: hidden; }

  /* Front */
  .card-front { left: 70px; top: 45px; background: var(--card-black); }
  .side-bar { position: absolute; width: 16px; height: 145px; background: var(--card-white); }
  .side-bar.left { left: 0; top: 135px; }
  .side-bar.right { right: 0; top: 70px; }

  .wordmark { display: flex; align-items: center; gap: 22px; }
  .wordmark-name {
    font-family: "Questrial", sans-serif;
    color: var(--text-white);
    letter-spacing: 0.42em;
    line-height: 1;
  }
  .wordmark-dot { background: var(--accent-red); }
  .tagline { font-family: "Questrial", sans-serif; color: var(--text-white); white-space: nowrap; }

  .card-front .brand { position: absolute; left: 0; right: 0; top: 140px; display: flex; flex-direction: column; align-items: center; }
  .card-front .wordmark-name { font-size: 92px; }
  .card-front .wordmark-dot { width: 18px; height: 18px; }
  .card-front .tagline { font-size: 17.5px; margin-top: 16px; }

  /* Back */
  .card-back { left: 470px; top: 465px; background: var(--card-white); }
  .back-band { position: absolute; left: 0; right: 0; top: 22px; height: 335px; background: var(--card-black); }
  .card-back .brand { position: absolute; left: 42px; top: 138px; display: flex; flex-direction: column; align-items: flex-start; }
  .card-back .wordmark { gap: 12px; }
  .card-back .wordmark-name { font-size: 54px; letter-spacing: 0.34em; }
  .card-back .wordmark-dot { width: 11px; height: 11px; }
  .card-back .tagline { font-size: 11px; margin-top: 10px; }

  .contact { position: absolute; left: 345px; top: 105px; color: var(--text-white); }
  .person-name { font-family: "Libre Baskerville", serif; font-size: 22px; }
  .person-role { font-family: "Arimo", sans-serif; font-size: 18px; margin-top: 4px; }
  .contact-list { list-style: none; margin-top: 26px; font-family: "Questrial", sans-serif; font-size: 12.5px; }
  .contact-list li { display: flex; align-items: center; height: 20px; }
  .contact-list svg { width: 14px; height: 14px; margin-right: 20px; fill: var(--accent-red); flex-shrink: 0; }
</style>
</head>
<body>
<main class="canvas">

  <section class="card card-front" aria-label="Card front">
    <span class="side-bar left"></span>
    <span class="side-bar right"></span>
    <div class="brand">
      <div class="wordmark">
        <span class="wordmark-name">PRCI</span>
        <span class="wordmark-dot"></span>
      </div>
      <p class="tagline">Plaster &amp; Resonance Craftworks Incorporated</p>
    </div>
  </section>

  <section class="card card-back" aria-label="Card back">
    <div class="back-band"></div>
    <div class="brand">
      <div class="wordmark">
        <span class="wordmark-name">PRCI</span>
        <span class="wordmark-dot"></span>
      </div>
      <p class="tagline">Plaster &amp; Resonance Craftworks Incorporated</p>
    </div>

    <div class="contact">
      <p class="person-name">Martin Hale</p>
      <p class="person-role">Director</p>
      <ul class="contact-list">
        <li><svg viewBox="0 0 16 16"><path d="M1 6c0-3 3-4 7-4s7 1 7 4v1h-4V5H5v2H1z"/><rect x="3" y="8" width="10" height="6" rx="1"/></svg>xxxx-xxxx</li>
        <li><svg viewBox="0 0 16 16"><path d="M8 1 1 8h2v7h4v-4h2v4h4V8h2z"/></svg>48 Lathe St. Harbor City</li>
        <li><svg viewBox="0 0 16 16"><rect x="4" y="1" width="8" height="14" rx="1.5"/></svg>xxxx-xxxx</li>
        <li><svg viewBox="0 0 16 16"><path d="M1 3h14v1L8 9 1 4z"/><path d="M1 6l7 5 7-5v7H1z"/></svg>hello@prci-works.com</li>
        <li><svg viewBox="0 0 16 16"><path fill-rule="evenodd" d="M8 1a7 7 0 1 1 0 14A7 7 0 0 1 8 1zm0 1.3A5.7 5.7 0 0 0 2.3 7.3h2.6C5 5 5.6 3.3 6.5 2.5 7 2.4 7.5 2.3 8 2.3zm0 0c.9 0 1.9 2 2 5H6c.1-3 1.1-5 2-5zM2.3 8.7A5.7 5.7 0 0 0 6.5 13.5C5.6 12.7 5 11 4.9 8.7zm3.7 0c.1 3 1.1 5 2 5s1.9-2 2-5zm5.1 0c-.1 2.3-.7 4-1.6 4.8a5.7 5.7 0 0 0 4.2-4.8zm0-1.4h2.6A5.7 5.7 0 0 0 9.5 2.5c.9.8 1.5 2.5 1.6 4.8z"/></svg>www.prci-works.com</li>
      </ul>
    </div>
  </section>

</main>
</body>
</html>
```